Feature Nomination Banner

Create a 600 x 160 banner advertisement for Counsel Ledger Quarterly’s feature story nominations. We’ve included the Counsel Ledger Quarterly logo (black and white versions) for inclusion.
Headline: Now Accepting Nominations for 2024 Features
Nominate an Outstanding Lawyer or Law Firm Today!

```html
<!DOCTYPE html>
<html lang="en">
<head>
<meta charset="utf-8">
<title>Counsel Ledger Quarterly – Feature Nomination Banners</title>
<link rel="stylesheet" href="https://fonts.googleapis.com/css2?family=Playfair+Display:wght@400;700&display=swap">
<style>
  :root {
    --navy: #35316b;
    --ink: #1d1c1b;
    --gold: #b39a5f;
    --white: #ffffff;
    --page: #ffffff;
    --suit-dark: #2a2c33;
    --suit-light: #8a8c93;
  }
  html, body {
    margin: 0;
    width: 1029px;
    height: 1200px;
    overflow: hidden;
    background: var(--page);
  }
  .banner-set {
    position: absolute;
    left: 0;
    top: 0;
    width: 600px;
    height: 700px;
    transform: scale(1.715);
    transform-origin: 0 0;
  }
  .banner {
    position: absolute;
    top: 50px;
    width: 160px;
    height: 600px;
    overflow: hidden;
    font-family: "Playfair Display", Georgia, serif;
    color: var(--white);
    text-align: center;
  }
  .banner--left { left: 42px; background: var(--ink); }
  .banner--middle { left: 220px; background: var(--ink); }
  .banner--right { left: 398px; background: var(--navy); }

  .banner__backdrop { position: absolute; left: 0; top: 0; width: 160px; height: 600px; }

  .brand {
    position: absolute;
    left: 0;
    top: 24px;
    width: 160px;
  }
  .brand__name {
    font-weight: 700;
    font-size: 8.6px;
    letter-spacing: 0.4px;
    line-height: 1;
  }
  .brand__rule {
    width: 112px;
    height: 0.6px;
    margin: 4px auto 0;
    background: var(--white);
    opacity: 0.6;
  }

  .headline {
    position: absolute;
    left: 0;
    width: 160px;
    margin: 0;
    font-weight: 700;
    font-size: 18.5px;
    line-height: 23.6px;
    text-transform: uppercase;
  }
  .headline__accent { color: var(--gold); }

  .subline {
    position: absolute;
    left: 0;
    width: 160px;
    margin: 0;
    font-weight: 400;
    font-size: 19px;
    line-height: 25.6px;
  }

  .cta {
    position: absolute;
    left: 50%;
    transform: translateX(-50%);
    width: 129px;
    height: 28px;
    border-radius: 14px;
    font-weight: 700;
    font-size: 13px;
    line-height: 28px;
    text-transform: uppercase;
    color: var(--white);
  }
  .cta--gold { background: var(--gold); }
  .cta--navy { background: var(--navy); }

  .portrait {
    position: absolute;
    background:
      radial-gradient(ellipse 30% 22% at 50% 18%, #c9a58e 0%, #9c8576 60%, transparent 100%),
      linear-gradient(180deg, transparent 0%, transparent 30%, var(--suit-light) 31%, var(--suit-dark) 55%, var(--suit-dark) 100%);
    border-radius: 40px 40px 0 0;
  }
  .banner--left .portrait { left: 12px; top: 400px; width: 136px; height: 200px; }
  .banner--middle .portrait,
  .banner--right .portrait { left: 14px; top: 345px; width: 136px; height: 255px; }
</style>
</head>
<body>
<div class="banner-set">

  <section class="banner banner--left">
    <svg class="banner__backdrop" viewBox="0 0 160 600" aria-hidden="true">
      <path d="M0 0 H160 V190 C110 200 55 208 0 216 Z" fill="var(--navy)"/>
      <path d="M62 208 C100 200 135 194 160 186 V196 C130 202 95 206 62 208 Z" fill="var(--gold)"/>
    </svg>
    <div class="brand"><div class="brand__name">COUNSEL LEDGER QUARTERLY</div><div class="brand__rule"></div></div>
    <h1 class="headline" style="top:85px">Now<br>Accepting<br><span class="headline__accent">Nominations</span><br>for 2024<br>Features</h1>
    <p class="subline" style="top:241px">Nominate an<br>Outstanding<br>Lawyer or Law<br>Firm Today!</p>
    <div class="cta cta--gold" style="top:363px">Click Here</div>
    <div class="portrait" role="img" aria-label="Portrait photo of a smiling attorney in a dark suit with arms crossed"></div>
  </section>

  <section class="banner banner--middle">
    <svg class="banner__backdrop" viewBox="0 0 160 600" aria-hidden="true">
      <path d="M0 365 L70 440 L160 520 V600 H0 Z" fill="var(--gold)"/>
    </svg>
    <div class="brand"><div class="brand__name">COUNSEL LEDGER QUARTERLY</div><div class="brand__rule"></div></div>
    <h1 class="headline" style="top:65px">Now<br>Accepting<br><span class="headline__accent">Nominations</span><br>for 2024<br>Features</h1>
    <p class="subline" style="top:183px">Nominate an<br>Outstanding<br>Lawyer or Law<br>Firm Today!</p>
    <div class="cta cta--navy" style="top:303px">Click Here</div>
    <div class="portrait" role="img" aria-label="Portrait photo of a smiling attorney in a dark suit with arms crossed"></div>
  </section>

  <section class="banner banner--right">
    <svg class="banner__backdrop" viewBox="0 0 160 600" aria-hidden="true">
      <path d="M0 365 L70 440 L160 520 V600 H0 Z" fill="var(--gold)"/>
    </svg>
    <div class="brand"><div class="brand__name">COUNSEL LEDGER QUARTERLY</div><div class="brand__rule"></div></div>
    <h1 class="headline" style="top:65px">Now<br>Accepting<br><span class="headline__accent">Nominations</span><br>for 2024<br>Features</h1>
    <p class="subline" style="top:183px">Nominate an<br>Outstanding<br>Lawyer or Law<br>Firm Today!</p>
    <div class="cta cta--gold" style="top:303px">Click Here</div>
    <div class="portrait" role="img" aria-label="Portrait photo of a smiling attorney in a dark suit with arms crossed"></div>
  </section>

</div>
</body>
</html>
```